Website Design and Build

This is a design and build of a dating site.

100% the most important thing is for the website to look good. I want this thing to be stunning and feel like a premium product so please only tender for the job if you excel at design and use of colours.

Theme is: premium, professional & uncluttered
Colour Scheme is: bright, fun and friendly but also reassuring and professional
 
Platforms: Initially just browser based (desktop and mobile) but if the proof of concept works we will roll it out to apps across the major platforms.

Marketing will be done primarily through organic online searches and content driven leads to a squeeze page, so SEO optimisation and experience with squeeze pages also a must.

Please include examples of sites you’ve done or other sites you think give a flavour of your vision for what this site will be. Any thoughts on palettes/colour scheme also useful.

I will provide the full brief to the successful designer.

Thank you for your time.

Industry/Entity Type

Dating

Coding

Coded - Design and coding required

Number of Pages Required

5+ page

Font styles to use
Sans Serif

Colors

Designer to choose colors to be used in the design.

Requirements
Must have
• Professional, Premium and uncluttered look.
• SEO optimisation.
• Squeeze page.
• A way to track different lead sources e.g. some of it will be content led to a squeeze page, some of it organic search engine hits, some of it unique referral links given to specific bloggers/influencers. I want to be able to track the success of all the different types of generating traffic to the site.
• I also want to be able to amend/update the site myself going forward so would like the spec/design to be clearly documented to allow me to do this.

```html
<!DOCTYPE html>
<html lang="en">
<head>
<meta charset="utf-8">
<title>Amorel — Dating</title>
<link rel="stylesheet" href="https://fonts.googleapis.com/css2?family=Open+Sans:ital,wght@0,400;0,600;0,700;1,400&display=swap">
<style>
:root{
  --header-from:#f2704a;
  --header-to:#e6416f;
  --purple:#6f2bc7;
  --band-from:#a15b8e;
  --band-to:#7430d2;
  --orange:#f06a3c;
  --yellow:#fcd116;
  --pink:#c2185b;
  --white:#ffffff;
  --text:#555555;
  --card-bg:#f4f4f4;
  --footer:#2e1b48;
  --footer-bottom:#231338;
  --footer-heading:#f5c518;
  --footer-link:#9b8fb3;
}
*{box-sizing:border-box;margin:0;padding:0}
html,body{width:1200px;height:2179px;overflow:hidden}
body{position:relative;background:var(--white);font-family:"Open Sans",Arial,sans-serif;color:var(--text)}
.abs{position:absolute}

/* header */
.site-header{position:absolute;left:0;top:0;width:1200px;height:80px;background:linear-gradient(90deg,var(--header-from),var(--header-to));z-index:5}
.brand{position:absolute;left:132px;top:18px;font-size:36px;font-weight:700;color:var(--white);letter-spacing:.5px}
.main-nav{position:absolute;left:603px;top:30px;display:flex;gap:0}
.main-nav a{position:absolute;color:var(--white);font-size:13px;text-decoration:none;white-space:nowrap}
.main-nav .active{text-decoration:underline}
.btn-pill{position:absolute;top:25px;height:31px;border-radius:16px;background:var(--white);color:#333;font-size:11.5px;display:flex;align-items:center;justify-content:center;gap:5px}

/* hero */
.hero-photo{position:absolute;left:0;top:0;width:1200px;height:690px;background:radial-gradient(ellipse at 45% 40%,#b8675c 0%,transparent 45%),linear-gradient(110deg,#3e6b4a 0%,#a88a4a 25%,#c8502e 50%,#e6a33a 70%,#d2432f 100%)}
.hero-wave{position:absolute;left:0;top:0}
.hero-title{position:absolute;left:131px;top:362px;font-size:40px;line-height:48px;font-weight:700;color:var(--white);text-transform:uppercase}
.hero-dots{position:absolute;left:545px;top:563px;display:flex;gap:18px}
.hero-dots span{width:14px;height:14px;border-radius:50%;background:#d6155a;border:2px solid var(--white)}
.hero-dots .on{background:#222}

/* welcome */
.section-title{position:absolute;left:0;width:1200px;text-align:center;font-weight:600;color:var(--purple);font-size:34px}
.welcome-text{position:absolute;left:132px;top:752px;width:936px;text-align:center;font-size:13.6px;line-height:24.5px;color:#555}

/* search & profiles */
.profiles-band{position:absolute;left:0;top:952px;width:1200px;height:460px;background:linear-gradient(90deg,var(--band-from),var(--band-to))}
.search-bar{position:absolute;left:132px;top:912px;width:936px;height:77px;border-radius:39px;background:var(--orange);z-index:2}
.search-title{position:absolute;left:34px;top:14px;font-size:36px;font-weight:700;color:var(--white);letter-spacing:.5px}
.field-label{position:absolute;top:13px;font-size:12.5px;color:var(--white)}
.field{position:absolute;top:31px;height:33px;border-radius:17px;background:var(--white);font-size:11.5px;color:#333;display:flex;align-items:center;padding-left:16px}
.field svg{position:absolute;right:10px;top:11px}
.find-btn{position:absolute;left:796px;top:34px;width:105px;height:34px;border-radius:17px;background:var(--yellow);color:#5a2a00;font-weight:700;font-size:13px;display:flex;align-items:center;justify-content:center}
.band-title{position:absolute;left:0;top:1052px;width:1200px;text-align:center;font-size:31px;font-weight:600;color:var(--white)}
.profile-card{position:absolute;top:1120px;width:155px;height:202px;background:var(--card-bg)}
.profile-photo{width:155px;height:150px;background:linear-gradient(160deg,#8a8a8a,#c9c5c0 55%,#6b6b6b)}
.profile-name{text-align:center;font-size:15px;color:#333;margin-top:8px;line-height:18px}
.profile-place{text-align:center;font-size:10.5px;color:#777;line-height:14px}
.carousel-arrow{position:absolute;top:1208px}

/* stories */
.story-box{position:absolute;left:132px;top:1537px;width:936px;height:233px;border-radius:88px;background:var(--card-bg);border:1px solid #dcdcdc}
.story-quote{position:absolute;left:60px;top:29px;width:816px;text-align:center;font-size:16.5px;line-height:27px;color:#444}
.story-name{position:absolute;left:0;top:120px;width:936px;text-align:center;font-size:13px;font-style:italic;color:var(--pink)}
.story-nav{position:absolute;left:442px;top:150px;display:flex;gap:14px}
.story-avatar{position:absolute;left:556px;top:1726px;width:88px;height:88px;border-radius:50%;border:5px solid #888;background:linear-gradient(140deg,#6b4a3a,#c59a7a 55%,#3a2a22)}

/* footer */
.footer-wave{position:absolute;left:0;top:1840px}
.footer-bottom{position:absolute;left:0;top:2128px;width:1200px;height:51px;background:var(--footer-bottom);text-align:center;font-size:11px;line-height:51px;color:#8a7fa3}
.footer-col{position:absolute;top:1978px}
.footer-col h3{font-size:16px;font-weight:400;color:var(--footer-heading);margin-bottom:10px;white-space:nowrap}
.footer-col li{list-style:none;font-size:11px;line-height:20.8px;color:var(--footer-link);white-space:nowrap}
.social{display:flex;gap:16px;margin-top:4px}
.social span{width:14px;height:14px;border-radius:50%;background:var(--footer-link)}
.newsletter{width:228px;height:34px;background:#e9e9ee;display:flex;align-items:center;padding-left:14px;font-size:11px;color:#333;position:relative}
.newsletter svg{position:absolute;right:14px;top:11px}
</style>
</head>
<body>

<div class="hero-photo" role="img" aria-label="Hero photograph: a happy young couple riding a colourful fairground swing ride"></div>
<svg class="hero-wave" width="1200" height="690" viewBox="0 0 1200 690">
  <path d="M0,528 C120,600 260,648 420,638 C620,626 780,565 940,585 C1050,600 1130,650 1200,672 L1200,690 L0,690 Z" fill="#ffffff"/>
</svg>

<header class="site-header">
  <div class="brand">Amorel</div>
  <nav class="main-nav">
    <a class="active" style="left:0">Profiles</a>
    <a style="left:67px">Success Stories</a>
    <a style="left:167px">Blog</a>
    <a style="left:216px">Support</a>
  </nav>
  <div class="btn-pill" style="left:883px;width:73px">
    <svg width="10" height="10" viewBox="0 0 10 10"><path d="M1,5 H6 M4,2.5 L6.5,5 L4,7.5 M7,1 H9 V9 H7" stroke="#333" stroke-width="1.4" fill="none"/></svg>Log in
  </div>
  <div class="btn-pill" style="left:963px;width:105px">
    <svg width="10" height="10" viewBox="0 0 10 10"><path d="M1,2 H5 M1,2 V9 H8 V5 M4,6 L9,1" stroke="#333" stroke-width="1.3" fill="none"/></svg>Register Now
  </div>
</header>

<h1 class="hero-title">Pellentesque blandit<br>lacus eget</h1>
<div class="hero-dots"><span class="on"></span><span></span><span></span><span></span></div>

<h2 class="section-title" style="top:706px">Welcome to Amorel</h2>
<p class="welcome-text">Nullam lorem urna, tempus eget mollis et, dapibus ac sem. Suspendisse gravida ornare erat sed pulvinar. Vestibulum luctus ex in egestas fringilla. Fusce nec leo ac urna pulvinar auctor. Mauris bibendum fringilla velit. Nulla in lorem at massa pellentesque posuere. Nulla tristique posuere molestie. Aliquam erat volutpat. Etiam quis aliquet risus. Duis ornare erat eget magna dapibus, in accumsan quam pharetra. Nam tempus, quam in bibendum vulputate, sapien dolor viverra nisl, vitae euismod elit turpis et nulla. Aliquam erat volutpat. Pellentesque blandit lacus eget nunc faucibus.</p>

<section class="profiles-band"></section>

<form class="search-bar">
  <div class="search-title">SEARCH</div>
  <span class="field-label" style="left:201px">Gender</span>
  <div class="field" style="left:201px;width:113px">Female
    <svg width="6" height="10" viewBox="0 0 6 10"><path d="M0,4 L3,1 L6,4 M0,6 L3,9 L6,6" fill="#666"/></svg></div>
  <span class="field-label" style="left:336px">Age from :</span>
  <div class="field" style="left:336px;width:81px">18
    <svg width="6" height="10" viewBox="0 0 6 10"><path d="M0,4 L3,1 L6,4 M0,6 L3,9 L6,6" fill="#666"/></svg></div>
  <span class="field-label" style="left:424px">Age to :</span>
  <div class="field" style="left:424px;width:82px">28
    <svg width="6" height="10" viewBox="0 0 6 10"><path d="M0,4 L3,1 L6,4 M0,6 L3,9 L6,6" fill="#666"/></svg></div>
  <span class="field-label" style="left:532px">Location</span>
  <div class="field" style="left:532px;width:241px">Country, City, Zipcode
    <svg width="8" height="11" viewBox="0 0 8 11"><path d="M4,11 C1,7 0,5.5 0,4 A4,4 0 0 1 8,4 C8,5.5 7,7 4,11 Z" fill="#444"/><circle cx="4" cy="4" r="1.5" fill="#fff"/></svg></div>
  <div class="find-btn">FIND NOW</div>
</form>

<h2 class="band-title">Latest Profiles</h2>
<svg class="carousel-arrow" style="left:47px" width="14" height="24" viewBox="0 0 14 24"><path d="M11,3 L3,12 L11,21" stroke="#fff" stroke-width="3" fill="none"/></svg>
<svg class="carousel-arrow" style="left:1138px" width="14" height="24" viewBox="0 0 14 24"><path d="M3,3 L11,12 L3,21" stroke="#fff" stroke-width="3" fill="none"/></svg>

<article class="profile-card" style="left:132px"><div class="profile-photo" role="img" aria-label="Profile photo of Jacob"></div><div class="profile-name">Jacob</div><div class="profile-place">New York</div></article>
<article class="profile-card" style="left:327px"><div class="profile-photo" role="img" aria-label="Profile photo of Sophia"></div><div class="profile-name">Sophia</div><div class="profile-place">Texas</div></article>
<article class="profile-card" style="left:523px"><div class="profile-photo" role="img" aria-label="Profile photo of William" style="background:linear-gradient(160deg,#9a9690,#cfcac2 55%,#3f6fa8)"></div><div class="profile-name">William</div><div class="profile-place">New Jersy</div></article>
<article class="profile-card" style="left:718px"><div class="profile-photo" role="img" aria-label="Profile photo of Olivia" style="background:linear-gradient(160deg,#4a4a4a,#a55a3a 55%,#d02040)"></div><div class="profile-name">Olivia</div><div class="profile-place">London</div></article>
<article class="profile-card" style="left:912px"><div class="profile-photo" role="img" aria-label="Profile photo of Jayden" style="background:linear-gradient(160deg,#3a3a3a,#9a8070 55%,#cfcfcf)"></div><div class="profile-name">Jayden</div><div class="profile-place">Sydney</div></article>

<h2 class="section-title" style="top:1482px">Success Stories</h2>
<blockquote class="story-box">
  <p class="story-quote">“ Etiam non nulla non turpis pharetra tincidunt sed ut lorem. Etiam bibendum eros at velit consectetur commodo. Ut auctor convallis ligula a finibus. Fusce lacinia rutrum nunc at vulputate. Quisque arcu erat, cursus a urna dictum, volutpat pretium nunc. ”</p>
  <cite class="story-name">John Cole and Madison</cite>
  <div class="story-nav">
    <svg width="20" height="16" viewBox="0 0 20 16"><path d="M19,8 H4 M9,2 L3,8 L9,14" stroke="#7a35c8" stroke-width="3" fill="none"/></svg>
    <svg width="20" height="16" viewBox="0 0 20 16"><path d="M1,8 H16 M11,2 L17,8 L11,14" stroke="#b5b5b5" stroke-width="3" fill="none"/></svg>
  </div>
</blockquote>
<div class="story-avatar" role="img" aria-label="Photo of the couple John Cole and Madison"></div>

<svg class="footer-wave" width="1200" height="288" viewBox="0 0 1200 288">
  <path d="M0,5 C140,68 300,96 450,92 C640,86 800,32 950,44 C1050,54 1130,118 1200,158 L1200,288 L0,288 Z" fill="#2e1b48"/>
</svg>

<footer>
  <div class="footer-col" style="left:132px"><h3>Information</h3><ul><li>Profiles</li><li>Success Stories</li><li>Blog</li><li>Support</li></ul></div>
  <div class="footer-col" style="left:283px"><h3>More Links</h3><ul><li>Regsiter Now</li><li>Sign In</li></ul></div>
  <div class="footer-col" style="left:436px"><h3>Aliquam dignissim</h3><ul><li>Nulla porttitor</li><li>Vestibulum</li><li>Duis hendrerit</li><li>Vestibulum</li></ul></div>
  <div class="footer-col" style="left:535px;top:2009px"><ul><li>Pellentesque</li><li>Nam elementum</li><li>Maecenas</li></ul></div>
  <div class="footer-col" style="left:684px"><h3>Follow us</h3><div class="social"><span></span><span></span><span></span><span></span></div></div>
  <div class="footer-col" style="left:840px"><h3>Newsletter Subscribe</h3>
    <div class="newsletter">Email Address
      <svg width="16" height="12" viewBox="0 0 16 12"><rect width="16" height="12" rx="1" fill="#2e1b48"/><path d="M1,1 L8,7 L15,1" stroke="#e9e9ee" stroke-width="1.4" fill="none"/></svg></div>
  </div>
  <div class="footer-bottom">Copyright © 2018 Amorel. All rights reserved.</div>
</footer>

</body>
</html>
```